ARC VOLLEY Business Card Project

I'd like to request a business card design for the new company I've launched.
The name of the company is "ARC VOLLEY" an indoor unmanned tennis practice facility.
We would like to see designs that use our brand identity color in the logo I've attached.
We hope to get the design with modern, luxurious and elegant tone and manner.
We hope the logo should not be too big.

Business card must have elements as below:
- Logo (One of the logos I've attached)
- Name (In Korean Text) : 박 서 윤
- Title (In Korean Text) : 대표
- Phone Number : 010-8472-3916
- Email Address : seoyun.park@arcvolley-example.co.kr
- Website : www.arcvolley-example.co.kr
- Instagram : arcvolley
- Address (In Korean text) : 경기도 용인시 수지구 풍덕천로 456 미래타워 5층 501호, 502호

Target Market(s)

Tennis amateurs in 20 to 40s

Industry/Entity Type

Sports, Hobby

Contact Information for Business Card

- Logo (One of the logos I've attached) - Name (In Korean Text) : 박 서 윤 - Title (In Korean Text) : 대표 - Phone Number : 010-8472-3916 - Email Address : seoyun.park@arcvolley-example.co.kr - Website : www.arcvolley-example.co.kr - Instagram : arcvolley - Address (In Korean text) : 경기도 용인시 수지구 풍덕천로 456 미래타워 5층 501호, 502호

Font styles to use
Sans Serif

Requirements
Must have
• Double sided
Nice to have
• Logo with intaglio or relief embossing
Should not have
• Logo should not be too big.

```html
<!DOCTYPE html>
<html lang="ko">
<head>
<meta charset="utf-8">
<title>ARC VOLLEY Business Card</title>
<link href="https://fonts.googleapis.com/css2?family=Noto+Sans+KR:wght@500;700&display=swap" rel="stylesheet">
<style>
  :root {
    --canvas: #e9eaec;
    --turf-light: #3f9a45;
    --turf-mid: #2f8a3a;
    --turf-dark: #24702f;
    --paper: #fbfbfc;
    --brand-green: #2b4a35;
    --ink-light: #ffffff;
    --shadow: rgba(0, 0, 0, 0.12);
  }
  * { box-sizing: border-box; margin: 0; padding: 0; }
  html, body {
    width: 1200px;
    height: 900px;
    overflow: hidden;
    background: var(--canvas);
    font-family: "Noto Sans KR", sans-serif;
  }
  .sheet {
    width: 1200px;
    height: 900px;
    display: flex;
    flex-direction: column;
    align-items: center;
    justify-content: center;
    gap: 50px;
  }
  .card {
    position: relative;
    width: 620px;
    height: 370px;
    border-radius: 4px;
    overflow: hidden;
    box-shadow: 0 8px 24px var(--shadow);
  }
  .card-front .turf-art {
    position: absolute;
    inset: 0;
    background:
      radial-gradient(ellipse at 78% 30%, var(--turf-light) 0%, transparent 60%),
      linear-gradient(160deg, var(--turf-mid) 0%, var(--turf-light) 50%, var(--turf-dark) 100%);
  }
  .holder {
    position: absolute;
    left: 52px;
    top: 44px;
    color: var(--ink-light);
  }
  .holder-name {
    font-size: 50px;
    font-weight: 700;
    letter-spacing: 0.06em;
    line-height: 1.1;
  }
  .holder-title {
    margin-top: 8px;
    font-size: 34px;
    font-weight: 700;
    line-height: 1.1;
  }
  .contact {
    position: absolute;
    left: 52px;
    right: 30px;
    bottom: 30px;
    list-style: none;
    color: var(--ink-light);
    font-size: 15px;
    font-weight: 500;
    line-height: 1.55;
  }
  .contact-item {
    display: flex;
    align-items: center;
    gap: 12px;
    white-space: nowrap;
  }
  .contact-icon { width: 14px; height: 14px; flex: none; }
  .card-back { background: var(--paper); }
  .brand-lockup {
    position: absolute;
    inset: 0;
    display: flex;
    align-items: center;
    justify-content: center;
    gap: 18px;
  }
  .brand-dot {
    width: 44px;
    height: 44px;
    border-radius: 50%;
    background: var(--brand-green);
  }
  .brand-name {
    color: var(--brand-green);
    font-size: 40px;
    font-weight: 700;
    letter-spacing: 0.04em;
  }
</style>
</head>
<body>
<main class="sheet">
  <section class="card card-front">
    <div class="turf-art" role="img" aria-label="Grass turf background with a tennis racket at the upper right and a yellow tennis ball"></div>
    <div class="holder">
      <p class="holder-name">박 서 윤</p>
      <p class="holder-title">대표</p>
    </div>
    <ul class="contact">
      <li class="contact-item">
        <svg class="contact-icon" viewBox="0 0 16 16" aria-hidden="true">
          <path fill="#fff" d="M3.5 1.5l2.3 0.4 0.9 3-1.5 1.2c0.8 1.7 2 2.9 3.7 3.7l1.2-1.5 3 0.9 0.4 2.3c-0.4 1.2-1.6 2-2.9 1.9C6 13 3 10 2 5.4 1.5 3.6 2.2 2.1 3.5 1.5z"/>
        </svg>
        <span>010-8472-3916</span>
      </li>
      <li class="contact-item">
        <svg class="contact-icon" viewBox="0 0 16 16" aria-hidden="true">
          <rect x="1" y="3" width="14" height="10" rx="1" fill="#fff"/>
          <path d="M1.5 4l6.5 5 6.5-5" fill="none" stroke="#2f8a3a" stroke-width="1.4"/>
        </svg>
        <span>seoyun.park@arcvolley-example.co.kr</span>
      </li>
      <li class="contact-item">
        <svg class="contact-icon" viewBox="0 0 16 16" aria-hidden="true">
          <circle cx="8" cy="8" r="6.5" fill="none" stroke="#fff" stroke-width="1.4"/>
          <path d="M1.5 8h13M8 1.5c-2.4 2.6-2.4 10.4 0 13M8 1.5c2.4 2.6 2.4 10.4 0 13" fill="none" stroke="#fff" stroke-width="1.2"/>
        </svg>
        <span>www.arcvolley-example.co.kr</span>
      </li>
      <li class="contact-item">
        <svg class="contact-icon" viewBox="0 0 16 16" aria-hidden="true">
          <circle cx="8" cy="8" r="5" fill="#fff"/>
        </svg>
        <span>arcvolley</span>
      </li>
      <li class="contact-item">
        <svg class="contact-icon" viewBox="0 0 16 16" aria-hidden="true">
          <path fill="#fff" d="M8 1a5 5 0 0 0-5 5c0 3.8 5 9 5 9s5-5.2 5-9a5 5 0 0 0-5-5zm0 7a2 2 0 1 1 0-4 2 2 0 0 1 0 4z"/>
        </svg>
        <span>경기도 용인시 수지구 풍덕천로 456 미래타워 5층 501호, 502호</span>
      </li>
    </ul>
  </section>

  <section class="card card-back">
    <div class="brand-lockup">
      <span class="brand-dot" aria-hidden="true"></span>
      <span class="brand-name">ARC VOLLEY</span>
    </div>
  </section>
</main>
</body>
</html>
```